An innovative software company needs a business card!

We need a business card design for our new innovative software company. Please use the details for the business card provided in business card details section. We will use the business card paper like: https://www.prindlecard.example/us/products/nfc/business-cards-plus.html Our company name: celvane We have already a logo and colors to use in business cards too ,

Target Market(s)

App & Sofware Development

Industry/Entity Type

Software

Contact Information for Business Card

Lukas Brenner, BSc.
Founder and Chief Code Wizard

Adress:
Pelzerweg 14/3/1708
A - 3274, Halmdorf

Tel: +43 (0) 664 219 53 08
Email: lukas.brenner@celvane.example
Web: www.celvane.example

Requirements
Must have
• - Use our logo
Nice to have
• It would be nice to have a nice picture on the backside. (About apps, software, technicals or funy stuff) - Use our colors as in business card (optional)

```html
<!DOCTYPE html>
<html lang="en">
<head>
<meta charset="utf-8">
<title>celvane business card</title>
<link rel="stylesheet" href="https://fonts.googleapis.com/css2?family=Open+Sans:wght@400;600;700&display=swap">
<style>
  :root {
    --stage: #e9e7e3;
    --card-dark: #25292c;
    --teal: #27b4d6;
    --text-light: #d9dcde;
    --divider: #6c7175;
    --circle-grey: #d4d4d4;
    --blue-deep: #1c2f9e;
    --blue-mid: #1f5fc9;
    --blue-bright: #39b8e6;
    --band: rgba(240, 242, 248, 0.92);
  }
  * { margin: 0; padding: 0; box-sizing: border-box; }
  html, body { width: 1200px; height: 780px; overflow: hidden; }
  body {
    background: var(--stage);
    font-family: "Open Sans", Arial, sans-serif;
    display: flex;
    align-items: center;
    justify-content: center;
    gap: 40px;
  }
  .card {
    width: 540px;
    height: 310px;
    border-radius: 18px;
    position: relative;
    overflow: hidden;
  }

  /* Front side */
  .card-front {
    background: var(--card-dark);
    display: flex;
    align-items: center;
    padding: 0 30px;
  }
  .brand-mark {
    width: 170px;
    flex: none;
    display: flex;
    align-items: center;
    gap: 10px;
  }
  .brand-dot {
    width: 26px; height: 26px;
    border-radius: 50%;
    background: var(--circle-grey);
    flex: none;
  }
  .brand-name {
    color: var(--teal);
    font-weight: 700;
    font-size: 30px;
    letter-spacing: -0.5px;
    white-space: nowrap;
  }
  .divider {
    width: 1px;
    height: 220px;
    flex: none;
    background: linear-gradient(to bottom, transparent, var(--divider) 20%, var(--divider) 80%, transparent);
    margin: 0 22px 0 4px;
  }
  .contact {
    color: var(--text-light);
    font-size: 13px;
    line-height: 1.5;
    white-space: nowrap;
  }
  .contact-name { color: var(--teal); font-size: 19px; font-weight: 600; line-height: 1.2; }
  .contact-role { font-size: 14px; margin-bottom: 20px; }
  .contact-address { margin-bottom: 18px; }
  .contact-label { color: var(--teal); }

  /* Back side */
  .card-back { background: var(--blue-deep); }
  .back-artwork {
    position: absolute; inset: 0;
    background:
      radial-gradient(circle at 22% 70%, var(--blue-bright) 0%, transparent 42%),
      radial-gradient(circle at 80% 25%, var(--blue-bright) 0%, transparent 35%),
      linear-gradient(135deg, var(--blue-deep), var(--blue-mid) 55%, var(--blue-deep));
  }
  .name-band {
    position: absolute;
    left: 0; right: 0;
    top: 90px; height: 130px;
    background: var(--band);
    display: flex;
    align-items: center;
    justify-content: center;
    gap: 16px;
  }
  .band-dot {
    width: 40px; height: 40px;
    border-radius: 50%;
    background: var(--teal);
  }
  .band-name {
    color: var(--teal);
    font-weight: 700;
    font-size: 64px;
    letter-spacing: -1px;
  }
</style>
</head>
<body>

  <section class="card card-front" aria-label="Card front">
    <div class="brand-mark">
      <span class="brand-dot"></span>
      <span class="brand-name">celvane</span>
    </div>
    <div class="divider"></div>
    <div class="contact">
      <p class="contact-name">Lukas Brenner, BSc.</p>
      <p class="contact-role">Founder and Chief Code Wizard</p>
      <p class="contact-address">Pelzerweg 14/3/1708<br>A - 3274, Halmdorf</p>
      <p><span class="contact-label">Tel:</span> +43 (0) 664 219 53 08</p>
      <p><span class="contact-label">Email:</span> lukas.brenner@celvane.example</p>
      <p><span class="contact-label">Web:</span> www.celvane.example</p>
    </div>
  </section>

  <section class="card card-back" aria-label="Card back">
    <div class="back-artwork" role="img" aria-label="Blue technology illustration of circuit lines, binary code, globes, device and security icons"></div>
    <div class="name-band">
      <span class="band-dot"></span>
      <span class="band-name">celvane</span>
    </div>
  </section>

</body>
</html>
```